Power Point Template Design for Consulting Company
Verdant Ridge Inc.
Helping Clients Achieve Explosive Sales
Need a slide master incorporating existing logo for all regular Power Point slide layout types (title, title and content, section header, two content, comparison, title only, blank, content with caption, picture with caption)
Corporate client presentations and professional association speaking engagements
Using Power Point 2007, Windows 7.0 O/S.
Not overpowering, prefer clean white backgrounds for better projection and printing results. Verdant Ridge Inc. Logo was designed on a previous project so all files available.
logo files in all formats
business card for reference and consistency
business letterhead for reference and consistency
business stationary coor and font for reference and consistency

```html
<!DOCTYPE html>
<html lang="en">
<head>
<meta charset="utf-8">
<title>Verdant Ridge Inc. – Title Slide Master</title>
<link rel="stylesheet" href="https://fonts.googleapis.com/css2?family=Arimo:wght@400;700&display=swap">
<style>
  :root {
    --page-bg: #e9e9e9;
    --slide-bg: #ffffff;
    --brand-deep: #0b4f9c;
    --brand-bright: #0a9fe0;
    --brand-text: #1677b5;
    --rule-grey: #8c8c8c;
    --rule-light: #f2f2f2;
    --placeholder-line: #8a8a8a;
    --ray-tone: #d9d9d9;
  }
  html, body {
    margin: 0;
    padding: 0;
    width: 1200px;
    height: 936px;
    overflow: hidden;
    background: var(--page-bg);
    font-family: "Arimo", Arial, sans-serif;
  }
  .slide {
    position: absolute;
    left: 0;
    top: 18px;
    width: 1200px;
    height: 900px;
    background: var(--slide-bg);
    overflow: hidden;
  }
  .light-rays {
    position: absolute;
    inset: 0;
    width: 1200px;
    height: 900px;
  }
  .side-band {
    position: absolute;
    left: 0;
    top: 0;
    width: 82px;
    height: 900px;
    background: linear-gradient(180deg, var(--brand-deep) 0%, #1170c4 25%, var(--brand-bright) 48%, #1170c4 70%, var(--brand-deep) 100%);
  }
  .side-rule {
    position: absolute;
    left: 82px;
    top: 0;
    width: 31px;
    height: 900px;
    background: linear-gradient(180deg, var(--rule-grey) 0%, #b5b5b5 25%, var(--rule-light) 50%, #b5b5b5 75%, var(--rule-grey) 100%);
  }
  .brand-mark {
    position: absolute;
    left: 67px;
    top: 79px;
    width: 144px;
    height: 141px;
    box-sizing: border-box;
    border: 7px solid #ffffff;
    border-radius: 18px;
    background: linear-gradient(160deg, var(--brand-bright) 0%, var(--brand-deep) 100%);
    box-shadow: 0 2px 6px rgba(0, 0, 0, 0.25);
  }
  .brand-name {
    position: absolute;
    left: 130px;
    top: 232px;
    margin: 0;
    font-size: 22px;
    font-weight: 700;
    color: var(--brand-text);
    white-space: nowrap;
  }
  .title-placeholder {
    position: absolute;
    left: 250px;
    top: 43px;
    width: 898px;
    height: 177px;
    box-sizing: border-box;
    border: 2px dashed var(--placeholder-line);
    display: flex;
    align-items: center;
    justify-content: center;
  }
  .title-placeholder h1 {
    margin: 0;
    font-size: 49px;
    font-weight: 700;
    color: var(--brand-text);
    letter-spacing: 0.5px;
  }
</style>
</head>
<body>
  <main class="slide">
    <svg class="light-rays" viewBox="0 0 1200 900" aria-hidden="true">
      <defs>
        <linearGradient id="ray-one" gradientUnits="userSpaceOnUse" x1="950" y1="0" x2="640" y2="530">
          <stop offset="0" stop-color="var(--ray-tone)" stop-opacity="0.9"/>
          <stop offset="1" stop-color="var(--ray-tone)" stop-opacity="0"/>
        </linearGradient>
        <linearGradient id="ray-two" gradientUnits="userSpaceOnUse" x1="1140" y1="0" x2="680" y2="565">
          <stop offset="0" stop-color="var(--ray-tone)" stop-opacity="0.9"/>
          <stop offset="1" stop-color="var(--ray-tone)" stop-opacity="0"/>
        </linearGradient>
        <linearGradient id="ray-three" gradientUnits="userSpaceOnUse" x1="1200" y1="320" x2="770" y2="625">
          <stop offset="0" stop-color="var(--ray-tone)" stop-opacity="0.9"/>
          <stop offset="1" stop-color="var(--ray-tone)" stop-opacity="0"/>
        </linearGradient>
      </defs>
      <polygon points="626,534 900,0 1007,0" fill="url(#ray-one)"/>
      <polygon points="672,565 1084,0 1200,0 1200,40" fill="url(#ray-two)"/>
      <polygon points="763,626 1200,244 1200,400" fill="url(#ray-three)"/>
    </svg>

    <div class="side-band"></div>
    <div class="side-rule"></div>

    <div class="brand-mark"></div>
    <p class="brand-name">Verdant Ridge Inc.</p>

    <div class="title-placeholder">
      <h1>CLICK TO ADD TITLE</h1>
    </div>
  </main>
</body>
</html>
```